BRVE branded stationary template

We need associated stationary to accompany our new logo.

The stationary design will be used on business cards, presentation slides and document templates so needs to be provided in an EPS format so that we can adapt it. The design MUST BE ADAPTABLE.

The logo colour is #4a4195 or RGB 85/68/141. Associated colours that can be used in this stationary should compliment this colour. Other colour choices - the preference would be dark and light purples, blues, black and greys. Done how you see fit.

We want the stationary to compliment the overall design of the logo, so clean sharp lines are what we are looking for. It doesn't need to be overly intricate in design - something simple that compliments the look and feel of the logo is what we want. More focused on lines and shapes around the stationary, not any additional logos or pictures.

Target Market(s)

UK housing providers

Industry/Entity Type

Business

Font styles to use
Sans Serif

Requirements
Must have
• Clean sharp appearance, nothing overly elaborate.

```html
<!DOCTYPE html>
<html lang="en">
<head>
<meta charset="utf-8">
<title>BRVE Business Card</title>
<link rel="stylesheet" href="https://fonts.googleapis.com/css2?family=Source+Sans+3:wght@400;600;700&family=Questrial&display=swap">
<style>
  :root {
    --purple: #554e97;
    --purple-dark: #463f86;
    --paper: #eeedf1;
    --ink: #4a4a4f;
    --rule: #8a8a92;
    --backdrop: #f2f2f4;
    --on-purple: #ececf3;
  }
  * { margin: 0; padding: 0; box-sizing: border-box; }
  html, body {
    width: 1105px; height: 1200px; overflow: hidden;
    background: var(--backdrop);
    font-family: "Source Sans 3", Arial, sans-serif;
  }
  .card {
    position: absolute; left: 180px; width: 746px; height: 425px;
    overflow: hidden;
  }
  .card--front { top: 120px; background: var(--paper); }
  .card--back { top: 655px; background: var(--purple); }

  .brand__mark { position: absolute; width: 52px; height: 52px; }
  .brand__name {
    position: absolute;
    font-family: "Source Sans 3", Arial, sans-serif;
    font-weight: 700; font-size: 78px; line-height: 1; letter-spacing: 2px;
  }
  .tagline {
    position: absolute; font-family: "Questrial", Arial, sans-serif;
    font-size: 22px; line-height: 28px; white-space: nowrap;
  }

  .card--front .brand__mark { left: 240px; top: 100px; background: var(--purple); }
  .card--front .brand__name { left: 318px; top: 84px; color: var(--purple); }
  .card--front .tagline { left: 200px; top: 164px; color: var(--purple); }

  .holder {
    position: absolute; right: 400px; top: 224px; text-align: right;
    color: var(--ink); font-size: 20px; line-height: 28px;
  }
  .holder__name {
    color: var(--purple); font-weight: 600; font-size: 26px; line-height: 30px;
  }
  .divider {
    position: absolute; left: 364px; top: 226px; width: 1px; height: 104px;
    background: var(--rule);
  }
  .contacts {
    position: absolute; left: 384px; top: 228px; list-style: none;
    color: var(--ink); font-size: 20px; line-height: 28px;
  }
  .contacts li { display: flex; align-items: center; gap: 12px; }
  .contacts svg { width: 18px; height: 18px; fill: var(--purple); flex: none; }

  .footer-band {
    position: absolute; left: 0; bottom: 0; width: 100%; height: 40px;
    background: var(--purple); border-top: 3px solid var(--purple-dark);
    color: var(--on-purple); font-size: 19px; letter-spacing: 8px;
    display: flex; align-items: center; justify-content: center;
  }

  .card--back .brand__mark { left: 250px; top: 193px; background: var(--on-purple); }
  .card--back .brand__name { left: 328px; top: 177px; color: var(--on-purple); }
  .card--back .tagline { left: 210px; top: 256px; color: var(--on-purple); }
</style>
</head>
<body>
  <section class="card card--front">
    <span class="brand__mark"></span>
    <span class="brand__name">BRVE</span>
    <p class="tagline">fresh thinking for better homes</p>

    <div class="holder">
      <p class="holder__name">DANIEL HARROW</p>
      <p>CEO/Founder</p>
      <p>2146 Larkspur Road</p>
      <p>Fairbanks, Alaska 99712</p>
    </div>
    <div class="divider"></div>
    <ul class="contacts">
      <li><svg viewBox="0 0 24 24"><path d="M6.6 10.8a15 15 0 0 0 6.6 6.6l2.2-2.2a1 1 0 0 1 1-.25 11.4 11.4 0 0 0 3.6.57 1 1 0 0 1 1 1V20a1 1 0 0 1-1 1A17 17 0 0 1 3 4a1 1 0 0 1 1-1h3.5a1 1 0 0 1 1 1c0 1.250.2 2.45.57 3.57a1 1 0 0 1-.25 1z"/></svg>614 205 7391</li>
      <li><svg viewBox="0 0 24 24"><path d="M7 1h10a2 2 0 0 1 2 2v18a2 2 0 0 1-2 2H7a2 2 0 0 1-2-2V3a2 2 0 0 1 2-2zm0 3v14h10V4zm5 15.5a1.2 1.2 0 1 0 0 2.4 1.2 1.2 0 0 0 0-2.4z"/></svg>752 390 1846</li>
      <li><svg viewBox="0 0 24 24"><path d="M7 2h8l3 3v4H7zM3 10h18a2 2 0 0 1 2 2v8a2 2 0 0 1-2 2H3a2 2 0 0 1-2-2v-8a2 2 0 0 1 2-2zm3 4v2h12v-2z"/></svg>538 127 6402</li>
      <li><svg viewBox="0 0 24 24"><path d="M2 5h20v14H2zm2 2v.5l8 5 8-5V7zm0 2.8V17h16V9.8l-8 5z"/></svg>hello@brvehomes.com</li>
    </ul>

    <div class="footer-band">www.brvehomes.com</div>
  </section>

  <section class="card card--back">
    <span class="brand__mark"></span>
    <span class="brand__name">BRVE</span>
    <p class="tagline">fresh thinking for better homes</p>
  </section>
</body>
</html>
```